Label for a new, ambitious & organic Loire valley still & sparkling white wine

In the uploaded items, I have added a brief which explains what I expect.

Ultimately, I need a complete visual identity which can be used on a website, on stationary, on packaging, clothes etc. First step is the front label of the wine bottles.

The estate is called Clos de XYZ (name to be releaved at a later stage) and is located in Vouvray appellation. It produces still and sparkling white wines based on the Chenin grape. Chenin is a niche grape compared to Sauvignon and Chardonnay. Customers are typically :
a) enlightened wine amateurs who value quality of product more than the price tag
b) chenin geeks – the vast majority of the world’s production is concentrated in south Africa and Loire valley so it is a bit of a monopoly
c) foodies – chenin is great for gastronomical food
d) people seeking natural / organic / biodynamic wines

The winey exists today but sells most of its wine to wholesalers and the quality is average. Its own brand is close to non-existent. I am keeping the name (clos de XYZ) but the wines will be of much higher quality. Market segment will be premium (for chenin wine) which corresponds to a 15-40 € price range.

As I am an outsider to the wine world, and have a much higher ambition than the average producer in that region, the graphical identity could include a “new kid on the block” / “innovation” / “stand out” effect. On the other hand, the Loire valley, the winery and our work methods are anchored in century long traditions. And the product is decidedly French. So the message should be “head in the sky and feet solidly anchored in the soil” or “a modern product anchored in tradition”.
The wine is organic, heading toward biodynamic and we will work hard to reduce, along the entire value chain, our environmental footprint.
We will work according to natural, traditional methods, letting the grapes, the soil and the weather express the stories they have to tell. The wines will not be ‘technical’ wines made with additives and technology.
The most iconic monument of the Vouvray wine area is the church tower which can be seen on the Lexorama page (also uploaded as part of the brief) : https://fr.lexorama-ency.org/article/Vouvray_%28AOC%29
The silhouette of the tower could be a salient graphical element – maybe even a totemic element.

The bottle shapes will be traditional ones because innovating on bottle design comes at a great cost. There is more impact/unit cost in the label. However, we will be exploring innovative bottling options for the sake of reducing the carbon footprint and most likely, there will not be much wiggle room for creative designs.
I like simple, clean (but not clinical), precise, stylish and timeless design.
We will produce still and sparking. For each category there will be 2 to 5 different wines. All wines will have in common : grape sort, Clos de XYZ and Vouvray appellation. Differences will be sparkling or not, dry or a little residual sugar, which parcel of land the grapes come from and how we made the wine. Sparkling or non-sparkling is obvious from the bottle. So the information that needs to be fitted on the front label (there will also be a more technical and regulated back label) is : Clos de XYZ, Vouvray, Chenin and then a difference name for each wine (cuvée in French). The latter could be the names of the plots/parcels of land. For example : Le Brolin

Target Market(s)

included in project description

Industry/Entity Type

wine

Requirements
Must have
• a more or less stylized profile of the Vouvray church tower
Nice to have
• a little V notch at the top of the label which suggests the 2 Vs of Vouvray

```html
<!DOCTYPE html>
<html lang="en">
<head>
<meta charset="utf-8">
<title>Clos de XYZ – Front Label Proof</title>
<link rel="stylesheet" href="https://fonts.googleapis.com/css2?family=Playfair+Display:wght@400;700&family=Oranienbaum&family=Allura&family=Pathway+Gothic+One&family=Arimo&family=Oswald:wght@700&display=swap">
<style>
  :root {
    --green: #72bf44;
    --green-soft: #c9e6b4;
    --gold: #d79a2b;
    --ink: #4a4a4a;
    --black: #000000;
    --alert: #ed1c24;
    --trim: #ec2c8f;
    --paper: #ffffff;
  }
  html, body {
    margin: 0;
    padding: 0;
    width: 1200px;
    height: 1059px;
    overflow: hidden;
    background: var(--paper);
  }
  .proof-sheet { display: block; width: 1200px; height: 1059px; }
  .measure-line { stroke: var(--black); stroke-width: 1.4; fill: none; }
  .measure-label { font-family: "Pathway Gothic One", sans-serif; font-size: 20px; fill: var(--black); }
  .trim-line { stroke: var(--trim); stroke-width: 1; fill: none; }
  .estate-name { font-family: "Playfair Display", serif; font-weight: 700; font-size: 84px; fill: var(--ink); }
  .grape-badge { fill: var(--green); }
  .grape-icon { fill: var(--paper); }
  .grape-name { font-family: "Playfair Display", serif; font-size: 24px; fill: var(--paper); letter-spacing: 0.5px; }
  .appellation { font-family: "Playfair Display", serif; font-size: 31px; fill: var(--ink); letter-spacing: 1px; }
  .type-ribbon { fill: var(--gold); }
  .type-name { font-family: "Oranienbaum", serif; font-size: 80px; fill: var(--paper); letter-spacing: 1px; }
  .style-name { font-family: "Allura", cursive; font-size: 76px; fill: var(--gold); }
  .legal-text { font-family: "Pathway Gothic One", sans-serif; font-size: 25px; fill: var(--black); }
  .note-text { font-family: "Arimo", sans-serif; font-size: 16px; fill: var(--black); }
  .note-line { stroke: var(--alert); stroke-width: 1.2; fill: none; }
  .note-dot { fill: var(--alert); }
  .swatch-label { font-family: "Arimo", sans-serif; font-size: 13px; fill: var(--black); }
  .stamp-ring { fill: none; stroke: var(--alert); stroke-width: 7; }
  .stamp-mark { fill: var(--alert); }
  .stamp-text { font-family: "Oswald", sans-serif; font-weight: 700; font-size: 36px; fill: var(--alert); letter-spacing: 1px; }
</style>
</head>
<body>
<svg class="proof-sheet" viewBox="0 0 1200 1059" xmlns="http://www.w3.org/2000/svg">
  <defs>
    <linearGradient id="landscape-tone" x1="0" y1="0" x2="0" y2="1">
      <stop offset="0" stop-color="#e9f4e0"/>
      <stop offset="0.45" stop-color="#e3f1d8"/>
      <stop offset="0.52" stop-color="#c9e6b4"/>
      <stop offset="0.72" stop-color="#d8edc9"/>
      <stop offset="1" stop-color="#ffffff"/>
    </linearGradient>
    <path id="stamp-arc" d="M 990 200 A 96 96 0 1 1 1162 200"/>
  </defs>

  <!-- dimensions -->
  <g class="dimensions">
    <text class="measure-label" x="444" y="62" text-anchor="middle">9 cm</text>
    <path class="measure-line" d="M127 76 H763 M127 70 V82 M763 70 V82"/>
    <path class="measure-line" d="M56 147 V997 M50 147 H62 M50 997 H62"/>
    <text class="measure-label" transform="translate(42 572) rotate(-90)" text-anchor="middle">12 cm</text>
  </g>

  <!-- label artwork -->
  <g class="front-label">
    <rect x="105" y="126" width="680" height="576" fill="url(#landscape-tone)" role="img" aria-label="Green halftone engraving of the Vouvray church tower rising above the village rooftops, fading out towards the bottom"/>

    <text class="estate-name" x="172" y="264">CLOS</text>
    <text class="estate-name" x="172" y="351">DE XYZ</text>

    <circle class="grape-badge" cx="234" cy="549" r="56"/>
    <g class="grape-icon">
      <circle cx="225" cy="522" r="3.6"/><circle cx="234" cy="522" r="3.6"/><circle cx="243" cy="522" r="3.6"/>
      <circle cx="229.5" cy="529" r="3.6"/><circle cx="238.5" cy="529" r="3.6"/>
      <circle cx="234" cy="536" r="3.6"/><circle cx="234" cy="543" r="3.2"/>
      <rect x="233" y="511" width="2" height="7"/>
      <circle cx="238" cy="512" r="2.2"/>
    </g>
    <text class="grape-name" x="234" y="573" text-anchor="middle">CHENIN</text>

    <text class="appellation" x="710" y="677" text-anchor="end">Vouvray</text>

    <polygon class="type-ribbon" points="162,719 728,719 710,764 728,809 162,809 180,764"/>
    <text class="type-name" x="444" y="792" text-anchor="middle">WHITE WINE</text>

    <text class="style-name" x="446" y="880" text-anchor="middle">Sparkling</text>

    <text class="legal-text" x="162" y="962">X% VOL.</text>
    <text class="legal-text" x="728" y="962" text-anchor="end">XX ML</text>

    <rect class="trim-line" x="126" y="146.5" width="638" height="851"/>
  </g>

  <!-- annotations -->
  <g class="annotations">
    <circle class="note-dot" cx="700" cy="492" r="4.5"/>
    <path class="note-line" d="M700 492 H856"/>
    <text class="note-text" x="878" y="481">green color to</text>
    <text class="note-text" x="878" y="502">represent organic /</text>
    <text class="note-text" x="878" y="523">biodynamic feeling</text>

    <circle class="note-dot" cx="727" cy="764" r="4.5"/>
    <circle class="note-dot" cx="576" cy="863" r="4.5"/>
    <path class="note-line" d="M727 764 H822 V863 H576 M822 815 H856"/>
    <text class="note-text" x="878" y="808">will be a specific color for</text>
    <text class="note-text" x="878" y="829">each variation (flavors/type)</text>
  </g>

  <!-- colour swatches -->
  <g class="swatches">
    <rect x="878" y="926" width="72" height="50" fill="var(--green)"/>
    <rect x="971" y="926" width="72" height="50" fill="var(--gold)"/>
    <rect x="1064" y="926" width="72" height="50" fill="var(--black)"/>
    <text class="swatch-label" x="914" y="998" text-anchor="middle">PMS 368 C</text>
    <text class="swatch-label" x="1007" y="998" text-anchor="middle">PMS 7563 C</text>
    <text class="swatch-label" x="1100" y="998" text-anchor="middle">BLACK</text>
  </g>

  <!-- approval stamp -->
  <g class="approval-stamp">
    <circle class="stamp-ring" cx="1076" cy="146" r="70"/>
    <path class="stamp-mark" d="M1068 103 Q1076 96 1084 103 L1080 158 H1072 Z"/>
    <circle class="stamp-mark" cx="1076" cy="176" r="10"/>
    <text class="stamp-text"><textPath href="#stamp-arc" startOffset="50%" text-anchor="middle">FOR APPROVAL</textPath></text>
  </g>
</svg>
</body>
</html>
```